Law Office Business Card

We need a business card design to include the following information:
Name of Firm: Halvern Law Group, P.A.
Address: 2417 Osprey Ln, Ste 208, West Palm Beach, FL 33512
Phone: 561-390-7752
Fax: 561-390-7789
Website: http://www.bhalvernlaw.example

We Need a place for the Person's name and email address. Please start with the following:
Lorna K. Tibbett, Esq.
lorna@bhalvernlaw.example

Industry/Entity Type

Business

```html
<!DOCTYPE html>
<html lang="en">
<head>
<meta charset="utf-8">
<title>Halvern Law Group – Business Card</title>
<link rel="stylesheet" href="https://fonts.googleapis.com/css2?family=Cinzel:wght@400&family=Open+Sans:wght@400&display=swap">
<style>
  :root {
    --backdrop: #ece9e4;
    --card-top: #c4b8a3;
    --card-bottom: #5c5349;
    --ink-light: #ffffff;
    --ink-soft: rgba(255,255,255,0.88);
    --rule-light: rgba(255,255,255,0.55);
    --bronze: #8a7c6a;
    --bronze-dark: #6f6456;
    --paper: #ffffff;
  }
  * { margin: 0; padding: 0; box-sizing: border-box; }
  html, body { width: 1200px; height: 900px; overflow: hidden; }
  body { background: var(--backdrop); position: relative; font-family: "Open Sans", sans-serif; }

  .card { position: absolute; box-shadow: 0 6px 22px rgba(0,0,0,0.18); }

  /* Front side */
  .card-front {
    left: 238px; top: 62px; width: 556px; height: 342px;
    background: linear-gradient(to bottom, var(--card-top), var(--card-bottom));
    color: var(--ink-light);
  }
  .firm-name {
    position: absolute; left: 0; right: 0; top: 50px;
    text-align: center; font-family: "Cinzel", serif;
    font-size: 36px; letter-spacing: 1px; line-height: 1;
  }
  .attorney-name {
    position: absolute; left: 0; right: 0; top: 158px;
    text-align: center; font-family: "Cinzel", serif;
    font-size: 19px; letter-spacing: 1px; color: var(--ink-soft);
  }
  .front-rule {
    position: absolute; left: 0; right: 0; top: 203px;
    height: 1px; background: var(--rule-light);
  }
  .contact-row {
    position: absolute; top: 220px; left: 26px; right: 22px;
    display: flex; justify-content: space-between; align-items: flex-start;
  }
  .contact-group { display: flex; flex-direction: column; }
  .contact-icons { display: flex; justify-content: center; gap: 8px; height: 22px; margin-bottom: 16px; }
  .contact-icons svg { width: 22px; height: 22px; display: block; }
  .contact-lines { font-size: 13.5px; line-height: 23px; color: var(--ink-light); white-space: nowrap; }
  .contact-divider {
    width: 1px; height: 34px; margin-top: 44px;
    background: var(--rule-light); flex: none;
  }

  /* Back side */
  .card-back {
    left: 458px; top: 518px; width: 560px; height: 344px;
    background: var(--paper); color: var(--bronze);
  }
  .back-mark {
    position: absolute; left: 50%; top: 90px; transform: translateX(-50%);
    width: 90px; height: 90px; border: 2px solid var(--bronze);
  }
  .back-firm-name {
    position: absolute; left: 0; right: 0; top: 200px;
    text-align: center; font-family: "Cinzel", serif;
    font-size: 33px; letter-spacing: 1px; color: var(--bronze-dark); line-height: 1;
  }
  .back-web {
    position: absolute; left: 0; right: 0; top: 288px;
    display: flex; align-items: center; gap: 14px;
    font-family: "Cinzel", serif; font-size: 14px; letter-spacing: 1px; color: var(--bronze-dark);
  }
  .back-web::before, .back-web::after { content: ""; flex: 1; height: 1px; background: #a79c8d; }
</style>
</head>
<body>

<section class="card card-front" aria-label="Business card front">
  <div class="firm-name">HALVERN LAW GROUP</div>
  <div class="attorney-name">LORNA K. TIBBETT, ESQ.</div>
  <div class="front-rule"></div>

  <div class="contact-row">
    <div class="contact-group phones">
      <div class="contact-icons">
        <svg viewBox="0 0 22 22" aria-label="Phone"><circle cx="11" cy="11" r="11" fill="#fff"/><path d="M7.5 6.5c.6-.6 1.3-.5 1.7.1l.9 1.4c.3.5.2 1-.2 1.4l-.6.5c.5 1.2 1.5 2.2 2.7 2.7l.5-.6c.4-.4.9-.5 1.4-.2l1.4.9c.6.4.7 1.1.1 1.7l-.7.7c-.8.8-3 .2-5.1-1.9S6 8 6.8 7.2z" fill="#5c5349"/></svg>
        <svg viewBox="0 0 22 22" aria-label="Fax"><circle cx="11" cy="11" r="11" fill="#fff"/><rect x="8" y="5.5" width="6" height="4" fill="none" stroke="#5c5349" stroke-width="1.2"/><rect x="6" y="9" width="10" height="7" rx="1" fill="#5c5349"/><rect x="8.5" y="11" width="5" height="1" fill="#fff"/><rect x="8.5" y="13" width="5" height="1" fill="#fff"/></svg>
      </div>
      <div class="contact-lines">561-390-7752<br>561-390-7789</div>
    </div>

    <div class="contact-divider"></div>

    <div class="contact-group web">
      <div class="contact-icons">
        <svg viewBox="0 0 22 22" aria-label="Email"><circle cx="11" cy="11" r="11" fill="#fff"/><rect x="5.5" y="7" width="11" height="8" fill="#5c5349"/><path d="M5.5 7l5.5 4.5L16.5 7" fill="none" stroke="#fff" stroke-width="1"/></svg>
        <svg viewBox="0 0 22 22" aria-label="Website"><circle cx="11" cy="11" r="11" fill="#fff"/><circle cx="11" cy="11" r="5.5" fill="none" stroke="#5c5349" stroke-width="1.3"/><ellipse cx="11" cy="11" rx="2.3" ry="5.5" fill="none" stroke="#5c5349" stroke-width="1"/><path d="M5.5 11h11" stroke="#5c5349" stroke-width="1"/></svg>
      </div>
      <div class="contact-lines">lorna@bhalvernlaw.example<br>www.bhalvernlaw.example</div>
    </div>

    <div class="contact-divider"></div>

    <div class="contact-group address">
      <div class="contact-icons">
        <svg viewBox="0 0 22 22" aria-label="Location"><circle cx="11" cy="11" r="11" fill="#fff"/><path d="M11 5a4 4 0 0 0-4 4c0 3 4 7.5 4 7.5s4-4.5 4-7.5a4 4 0 0 0-4-4z" fill="#5c5349"/><circle cx="11" cy="9" r="1.5" fill="#fff"/></svg>
      </div>
      <div class="contact-lines">2417 Osprey Ln, Ste 208,<br>West Palm Beach, FL 33512</div>
    </div>
  </div>
</section>

<section class="card card-back" aria-label="Business card back">
  <div class="back-mark"></div>
  <div class="back-firm-name">HALVERN LAW GROUP</div>
  <div class="back-web">WWW.BHALVERNLAW.EXAMPLE</div>
</section>

</body>
</html>
```